Flyer design for webdesign company

create a flyer that can be printed or sent as an email. The flyer needs to be professional, modern and engaging.

Reason: opportunity for all designers to get their designs in.

Target Market(s)

business owners that do not have a website

Industry/Entity Type

It Company

Font styles to use
Sans Serif

```html
<!DOCTYPE html>
<html lang="en">
<head>
<meta charset="utf-8">
<title>Web Design Flyer</title>
<link rel="stylesheet" href="https://fonts.googleapis.com/css2?family=Montserrat:wght@300;400;900&family=Open+Sans:wght@300;400;600;700;800&display=swap">
<style>
  :root {
    --page: #e4e4e4;
    --charcoal: #26282b;
    --charcoal-soft: rgba(34, 36, 40, 0.8);
    --orange: #f0952c;
    --white: #ffffff;
    --ink: #1d1f22;
  }
  * { box-sizing: border-box; margin: 0; padding: 0; }
  html, body { width: 1200px; height: 800px; overflow: hidden; }
  body {
    background: var(--page);
    font-family: "Open Sans", Arial, sans-serif;
    display: flex; align-items: center; justify-content: center;
  }
  .flyer {
    position: relative;
    width: 540px; height: 760px;
    background: var(--charcoal);
    overflow: hidden;
    box-shadow: 0 10px 30px rgba(0,0,0,0.18);
  }
  .hero-photo {
    position: absolute; left: 0; top: 0; width: 100%; height: 640px;
    background: linear-gradient(160deg, #5d6a73 0%, #a9b6bf 22%, #dfe4e8 34%, #3d5366 52%, #22384c 72%, #1c2a36 100%);
  }
  .overlay { position: absolute; left: 0; top: 0; width: 100%; height: 100%; }
  .headline { position: absolute; left: 34px; top: 44px; color: var(--white); }
  .headline .verb {
    font-family: "Montserrat", Arial, sans-serif; font-weight: 900;
    color: var(--orange); font-size: 64px; line-height: 0.9; letter-spacing: 1px;
  }
  .headline .tag {
    font-family: "Montserrat", Arial, sans-serif; font-weight: 300;
    font-size: 22px; letter-spacing: 3px; margin-bottom: 18px;
  }
  .headline .make { margin-left: 70px; }
  .benefits {
    position: absolute; right: 22px; top: 238px; width: 228px;
    color: var(--white); font-size: 12px; line-height: 1.3; font-weight: 300;
  }
  .benefits p { margin-bottom: 7px; }
  .benefits .offer { font-weight: 700; text-transform: uppercase; }
  .benefits strong { font-weight: 700; }
  .price-band {
    position: absolute; left: 0; top: 530px; width: 100%; height: 74px;
    background: var(--orange);
    display: flex; align-items: center; padding: 0 26px; color: var(--white);
  }
  .devices { width: 74px; height: 44px; margin-right: 48px; }
  .price-only { font-size: 13px; margin-right: 6px; align-self: flex-start; margin-top: 22px; }
  .price { font-weight: 800; font-size: 54px; line-height: 1; }
  .price-unit { font-size: 13px; align-self: flex-end; margin: 0 0 14px 4px; }
  .per-day { margin-left: auto; text-align: right; line-height: 1.1; }
  .per-day small { font-size: 12px; display: block; }
  .per-day b { font-size: 24px; font-weight: 800; }
  .call-band {
    position: absolute; left: 0; top: 604px; width: 100%; height: 66px;
    background: var(--ink); color: var(--white); padding: 9px 26px 0 140px;
  }
  .call-band .pitch { font-size: 13px; font-weight: 300; }
  .call-band .phone { font-size: 24px; font-weight: 800; letter-spacing: 0.5px; }
  .footer {
    position: absolute; left: 0; top: 670px; width: 100%; height: 90px;
    background: var(--white);
    display: flex; align-items: center; justify-content: center;
  }
  .brand-name { font-size: 20px; font-weight: 600; color: var(--charcoal); }
</style>
</head>
<body>
  <main class="flyer">
    <div class="hero-photo" role="img" aria-label="Photo of a white keyboard and a tablet showing a business web app with a smiling professional"></div>

    <svg class="overlay" viewBox="0 0 540 760" aria-hidden="true">
      <polygon points="0,0 540,0 540,60 0,330" fill="rgba(30,32,36,0.82)"/>
      <polygon points="290,160 540,60 540,530 400,530" fill="var(--charcoal-soft)"/>
      <polygon points="0,440 160,530 0,530" fill="rgba(255,255,255,0.85)"/>
    </svg>

    <header class="headline">
      <div class="verb">Attract</div>
      <div class="tag">More Customers</div>
      <div class="verb make">Make</div>
      <div class="tag make">More Money</div>
    </header>

    <section class="benefits">
      <p>97% of people look online for businesses.</p>
      <p>You need a website.</p>
      <p>You're losing many customers by not having a website.</p>
      <p>Beat your competition with better visibility and credibility.</p>
      <p class="offer">Beautiful websites available now!</p>
      <p>Smart, clean website designs <strong>($3000 Value. No extra charge)</strong></p>
      <p>Limited to ONLY 4 WEBSITES per area. Don't miss out!</p>
      <p>Social Media setup options (Search &amp; Social)</p>
    </section>

    <section class="price-band">
      <svg class="devices" viewBox="0 0 74 44" aria-hidden="true">
        <rect x="22" y="4" width="50" height="36" rx="3" fill="none" stroke="#fff" stroke-width="2.5"/>
        <rect x="2" y="14" width="16" height="28" rx="3" fill="none" stroke="#fff" stroke-width="2.5"/>
      </svg>
      <span class="price-only">only</span>
      <span class="price">$99</span>
      <span class="price-unit">/month</span>
      <div class="per-day"><small>that's</small><b>$3.30</b><small>a day</small></div>
    </section>

    <section class="call-band">
      <p class="pitch">Stop wasting money on mailers and print advertising.</p>
      <p class="phone">CALL 1-800-555-0147</p>
    </section>

    <footer class="footer">
      <span class="brand-name">Brightpage Studio</span>
    </footer>
  </main>
</body>
</html>
```